Personal Trainer Business Card Design and Logo

I am a Personal Trainer and passionate in helping obese kids loose weight, I would love a business card design for my business called TOLV Fitness.
TOLV Ftiness stands for Tall Oaks Lively Ventures, I would like the business card to be bright and appealing to the kids as well as the parents.
I would also love a logo designs witch is simple but affective.

Things I would like in the business card
- Kids playing and being happy (no cartoon characters)
- The card should be bright and colourful
- My name, Bartholomew Van Hoek Personal Trainer
- Contact number 0472615809
- Email address tolvfitness@wexmail.test

Things I would like in the logo
-colourful design which incorporate kids
- your creative logo

thanks for all your entries
kind regards Bart
Updates

loving all the designs, you are all so talented.

could you please read the updated brief

kind regards

Bart

Reason: Loving the designs, but needs more modification kind reagrds Bart

Target Market(s)

Kids and Parents

Industry/Entity Type

Business

Contact Information for Business Card

TOLV Fitness for kids

Tall Oaks Lively Ventures

Bart Van Hoek Personal Trainer
0472615809

Requirements
Must have
• Kids laughing and happy, tolv fitness logo, Bart Van Hoek Personal Trainer, 0472615809,tolvfitness@wexmail.test, colourful and bright.
Nice to have
• pulse council mark

```html
<!DOCTYPE html>
<html lang="en">
<head>
<meta charset="utf-8">
<title>TOLV Fitness – Business Card</title>
<link rel="stylesheet" href="https://fonts.googleapis.com/css2?family=Ubuntu:ital,wght@0,300;0,400;0,500;1,500;1,700&display=swap">
<style>
  :root {
    --frame: #0d0d0d;
    --paper: #f2f1ed;
    --paper-shade: #e6e5e0;
    --ink: #1c1c1c;
    --brand-ink: #2a2a2a;
    --trainer-blue: #1f5d9c;
    --contact-blue: #3399cc;
    --splash-blue: #a9d6ea;
    --splash-soft: #d6ecf5;
  }
  html, body {
    margin: 0;
    padding: 0;
    width: 1200px;
    height: 695px;
    overflow: hidden;
    background: #ffffff;
  }
  .card {
    position: relative;
    width: 1200px;
    height: 695px;
    box-sizing: border-box;
    border: 14px solid var(--frame);
    background:
      radial-gradient(circle at 30% 40%, var(--paper) 0%, var(--paper-shade) 100%);
    font-family: "Ubuntu", sans-serif;
    color: var(--ink);
    overflow: hidden;
  }
  .splash {
    position: absolute;
    left: 690px;
    top: 30px;
    width: 490px;
    height: 540px;
    border-radius: 46% 40% 44% 52%;
    background: radial-gradient(ellipse at 55% 45%, var(--splash-blue) 0%, var(--splash-soft) 55%, rgba(214,236,245,0) 75%);
  }
  .kids-photo {
    position: absolute;
    left: 766px;
    top: 284px;
    width: 390px;
    height: 383px;
    border-radius: 40% 40% 6px 6px;
    background: linear-gradient(180deg, #c9a07e 0%, #b98c6e 30%, #c96f78 55%, #6f8a74 75%, #3d6fb2 100%);
    opacity: 0.85;
  }
  .brand {
    position: absolute;
    left: 170px;
    top: 42px;
    display: flex;
    align-items: center;
    gap: 22px;
  }
  .brand-dot {
    width: 48px;
    height: 48px;
    border-radius: 50%;
    background: var(--brand-ink);
  }
  .brand-name {
    font-size: 60px;
    font-weight: 400;
    color: var(--brand-ink);
    line-height: 1;
  }
  .tagline {
    position: absolute;
    left: 240px;
    top: 128px;
    font-size: 21px;
    font-weight: 300;
    color: var(--brand-ink);
  }
  .contact {
    position: absolute;
    right: 544px;
    top: 262px;
    text-align: right;
  }
  .contact-name {
    font-size: 52px;
    font-weight: 400;
    line-height: 1.1;
    margin: 0;
  }
  .contact-role {
    font-size: 36px;
    font-weight: 700;
    font-style: italic;
    color: var(--trainer-blue);
    margin: 2px 0 0;
  }
  .contact-line {
    display: flex;
    justify-content: flex-end;
    align-items: center;
    gap: 10px;
    font-size: 38px;
    font-weight: 500;
    font-style: italic;
    color: var(--contact-blue);
  }
  .contact-phone { margin-top: 26px; }
  .contact-email { margin-top: 24px; }
  .icon { flex: none; }
</style>
</head>
<body>
  <main class="card">
    <div class="splash" role="img" aria-label="Soft blue watercolour splash"></div>
    <div class="kids-photo" role="img" aria-label="Photo of two happy children running and jumping over colourful hoops"></div>

    <header class="brand">
      <span class="brand-dot"></span>
      <span class="brand-name">TOLV Fitness</span>
    </header>
    <p class="tagline" style="margin:0">Tall Oaks Lively Ventures</p>

    <section class="contact">
      <h1 class="contact-name">Bartholomew Van Hoek</h1>
      <p class="contact-role">Personal Trainer</p>
      <p class="contact-line contact-phone" style="margin-bottom:0">
        <svg class="icon" width="38" height="38" viewBox="0 0 24 24" aria-hidden="true">
          <path fill="#1c1c1c" d="M6.6 2.5c.6-.4 1.4-.3 1.8.3l2.2 3.3c.4.6.3 1.3-.2 1.8l-1.3 1.2c.9 2 2.6 3.8 4.6 4.8l1.3-1.3c.5-.5 1.2-.6 1.8-.2l3.3 2.1c.6.4.8 1.2.4 1.8l-1.3 2.2c-.6 1-1.8 1.5-3 1.2C10.3 18.3 5.6 13.6 4.2 7.7c-.3-1.2.2-2.4 1.2-3z"/>
        </svg>
        <span>0472615809</span>
      </p>
      <p class="contact-line contact-email" style="margin-bottom:0">
        <svg class="icon" width="46" height="34" viewBox="0 0 46 34" aria-hidden="true">
          <rect x="1" y="1" width="44" height="32" fill="#1c1c1c"/>
          <path d="M2 3 L23 19 L44 3" fill="none" stroke="#f2f1ed" stroke-width="2.5"/>
          <path d="M2 32 L17 15 M44 32 L29 15" fill="none" stroke="#f2f1ed" stroke-width="2"/>
        </svg>
        <span>tolvfitness@wexmail.test</span>
      </p>
    </section>
  </main>
</body>
</html>
```